Invitation to Retail Shopping Event

-Must include logo
-Can contain product pictures depending on design
-I prefer any graphics to be my own product pictures
-Should include the following language:
Sip and Shop
Thursday, November 18
11 to 1 pm
487 Birch Lane
Come enjoy sips, snacks and shopping! Be the first to preview our new winter collection and get an early start on your holiday gifting.
Please RSVP to 415-382-9061 or info@brivettenw.com

```html
<!DOCTYPE html>
<html lang="en">
<head>
<meta charset="utf-8">
<title>Brivette NW — Sip &amp; Shop Invitation</title>
<link rel="stylesheet" href="https://fonts.googleapis.com/css2?family=Arimo:wght@400&family=Pinyon+Script&display=swap">
<style>
  :root {
    --page: #ffffff;
    --blush: #ebd3cd;
    --card-foot: #fafafa;
    --ink-grey: #5f5f5f;
    --script-grey: #7a7a7a;
    --date-brown: #8d4a3b;
    --note-rose: #b06b5a;
    --body-grey: #575757;
    --gold-light: #f2d98a;
    --gold-deep: #c49a2c;
    --tray-light: #e9cf96;
    --tray-dark: #5a4a33;
    --slipper-fur: #eadbd2;
    --slipper-sole: #8f7f8a;
  }
  * { margin: 0; padding: 0; box-sizing: border-box; }
  html, body { width: 1200px; height: 1000px; overflow: hidden; background: var(--page); }
  .canvas { position: relative; width: 1200px; height: 1000px; }

  .invitation {
    position: absolute; left: 284px; top: 20px; width: 638px; height: 958px;
    background: var(--card-foot);
    box-shadow: 6px 6px 12px rgba(0,0,0,0.18);
    overflow: hidden;
    font-family: "Arimo", Arial, sans-serif;
  }
  .invitation__field {
    position: absolute; left: 0; top: 0; width: 638px; height: 815px;
    background: var(--blush);
  }

  .brand {
    position: absolute; left: 120px; top: 128px; width: 398px; text-align: center;
    color: var(--ink-grey); font-family: "Arimo", Arial, sans-serif; font-weight: 400;
    font-size: 40px; line-height: 1; letter-spacing: 1px;
  }

  .event-title {
    position: absolute; left: 180px; top: 285px; width: 300px; text-align: center;
    font-family: "Pinyon Script", cursive; font-size: 58px; color: var(--script-grey);
    transform: rotate(-20deg);
  }

  .event-details { position: absolute; left: 234px; top: 440px; width: 380px; text-align: center; color: var(--date-brown); font-size: 24px; line-height: 29px; text-transform: uppercase; }
  .event-offer { position: absolute; left: 234px; top: 546px; width: 390px; text-align: center; color: var(--note-rose); font-size: 21.5px; line-height: 27px; text-transform: uppercase; }
  .event-intro { position: absolute; left: 0; top: 669px; width: 348px; text-align: center; color: var(--body-grey); font-size: 21.5px; line-height: 27px; }
  .rsvp { position: absolute; left: 0; top: 833px; width: 348px; text-align: center; color: var(--body-grey); font-size: 22px; line-height: 29.5px; }

  .product { position: absolute; }
  .product--earring-top { left: 594px; top: 145px; width: 44px; height: 95px; border-radius: 40px 0 0 40px; background: radial-gradient(circle at 60% 50%, var(--gold-light), var(--gold-deep)); }
  .product--earring { left: 536px; top: 272px; width: 102px; height: 108px; border-radius: 50%; background: radial-gradient(circle, var(--gold-light), var(--gold-deep)); }
  .product--tray { left: 0; top: 320px; width: 196px; height: 328px; border-radius: 0 50% 50% 0 / 0 50% 50% 0; background: radial-gradient(ellipse at 30% 50%, var(--tray-light), #d2b47a 70%, var(--tray-dark)); }
  .product--slippers { left: 356px; top: 650px; width: 282px; height: 290px; border-radius: 40% 10% 20% 35%; background: linear-gradient(160deg, var(--slipper-fur) 0%, #e2cfc6 55%, var(--slipper-sole) 100%); }
</style>
</head>
<body>
<div class="canvas">
  <article class="invitation">
    <div class="invitation__field"></div>

    <header class="brand">Brivette NW</header>

    <div class="product product--earring-top" role="img" aria-label="Gold floral earring with crystals"></div>
    <div class="product product--earring" role="img" aria-label="Gold floral earring with crystal centre"></div>
    <div class="product product--tray" role="img" aria-label="Round leopard-print tray with gold rim"></div>

    <h1 class="event-title">Sip &amp; Shop</h1>

    <p class="event-details">Thursday, November 18<br>11 to 1 PM<br>487 Birch Lane</p>
    <p class="event-offer">Come enjoy<br>sips, snacks and shopping!</p>

    <p class="event-intro">Be the first to preview<br>our new winter collection and<br>get an early start<br>on your holiday gifting.</p>

    <p class="rsvp">Please RSVP<br>415-382-9061<br>or info@brivettenw.com</p>

    <div class="product product--slippers" role="img" aria-label="Pair of plush pom-pom slide slippers in blush and mauve"></div>
  </article>
</div>
</body>
</html>
```